Brindel's Coating & Renewal Letterhead Design We want to revamp out old traditional letterhead with the new logo designs that are attached. We are working on getting all our company items from vehicles, business, cards, t-shirts, letterhead to match. This should include company colors, fonts, and flow of items that we have attached below.

Industry/Entity Type

Construction Company

Font styles to use
Sans Serif
Other font styles liked:
• Bold with outline

Colors
ec1f27
ffffff

Requirements
Must have
• Company Name: Brindel's Coating & Renewal
• Address: 4217 SW 83rd Ter Marlow Cove fl 33418
• Office Number: (954) 555-0194
• Email: Brindelrenewal@quorvane.com
• License Number: CGC8064392
Nice to have
• Company Colors: red, white, black, and grey

```html
<!DOCTYPE html>
<html lang="en">
<head>
<meta charset="utf-8">
<title>Brindel's Coating &amp; Renewal — Letterhead</title>
<link rel="stylesheet" href="https://fonts.googleapis.com/css2?family=Arimo:wght@400;700&family=Tinos:wght@400;700&display=swap">
<style>
  :root {
    --brand-red: #ec1f27;
    --brand-red-deep: #b8121a;
    --paper: #ffffff;
    --backdrop: #d9dcdd;
    --ink-grey: #7a7a7a;
    --ink-dark: #1e1e1e;
    --rule-grey: #d4d4d4;
  }
  * { box-sizing: border-box; margin: 0; padding: 0; }
  html, body {
    width: 1200px; height: 784px; overflow: hidden;
    background: var(--backdrop);
  }
  .canvas {
    position: relative; width: 1200px; height: 784px;
    display: flex; align-items: center; justify-content: center;
  }
  .letterhead {
    position: relative; width: 572px; height: 740px;
    background: var(--paper);
    box-shadow: 0 2px 10px rgba(0,0,0,0.12);
  }
  .side-band {
    position: absolute; left: 16px; top: 0; bottom: 0; width: 11px;
    background: linear-gradient(90deg, var(--brand-red-deep), var(--brand-red) 55%, var(--brand-red-deep));
  }
  .company-name {
    position: absolute; left: 62px; top: 38px;
    font-family: "Arimo", sans-serif; font-weight: 700;
    color: var(--brand-red); text-transform: uppercase;
    line-height: 1.0; letter-spacing: 0.5px;
  }
  .company-name .line-main { display: block; font-size: 34px; }
  .company-name .line-sub { display: block; font-size: 17px; margin-top: 3px; }
  .contact-block {
    position: absolute; right: 30px; top: 40px; width: 150px;
    padding-left: 12px; border-left: 1px solid var(--rule-grey);
    font-family: "Tinos", serif; font-size: 9px; line-height: 1.45;
    color: var(--ink-grey);
  }
  .contact-item { display: flex; align-items: flex-start; gap: 5px; }
  .contact-item svg { flex: none; width: 8px; height: 8px; margin-top: 2px; }
  .contact-address { color: var(--brand-red); font-weight: 700; margin-bottom: 1px; }
  .letter-body {
    position: absolute; left: 62px; top: 150px; width: 330px;
    font-family: "Arimo", sans-serif; font-size: 10.5px; line-height: 1.42;
    color: var(--ink-grey);
  }
  .letter-body p { margin-bottom: 18px; }
  .signature-area {
    position: absolute; left: 62px; top: 520px; width: 170px; height: 70px;
    background: linear-gradient(90deg, rgba(120,120,120,0.10), rgba(120,120,120,0.03));
    border-radius: 4px;
  }
</style>
</head>
<body>
<div class="canvas">
  <article class="letterhead">
    <div class="side-band"></div>

    <header class="company-name" aria-label="Brindel's Coating &amp; Renewal">
      <span class="line-main">Brindel's</span>
      <span class="line-sub">Coating &amp; Renewal</span>
    </header>

    <address class="contact-block">
      <div class="contact-item contact-address">
        <svg viewBox="0 0 10 10"><circle cx="5" cy="5" r="5" fill="#ec1f27"/><circle cx="5" cy="4.3" r="1.6" fill="#fff"/></svg>
        <span>4217 SW 83rd Ter<br>Marlow Cove, fl 33418</span>
      </div>
      <div class="contact-item">
        <svg viewBox="0 0 10 10"><circle cx="5" cy="5" r="5" fill="#ec1f27"/><rect x="3.4" y="2.4" width="3.2" height="5.2" rx="0.6" fill="#fff"/></svg>
        <span>(954) 555-0194</span>
      </div>
      <div class="contact-item">
        <svg viewBox="0 0 10 10"><circle cx="5" cy="5" r="5" fill="#ec1f27"/><path d="M3.5 5.2l1.1 1.1 2-2.4" stroke="#fff" stroke-width="1.1" fill="none"/></svg>
        <span>License: CGC8064392</span>
      </div>
      <div class="contact-item">
        <svg viewBox="0 0 10 10"><circle cx="5" cy="5" r="5" fill="#ec1f27"/><rect x="2.5" y="3.2" width="5" height="3.6" fill="#fff"/><path d="M2.5 3.2L5 5.2l2.5-2" stroke="#ec1f27" stroke-width="0.7" fill="none"/></svg>
        <span>Brindelrenewal@quorvane.com</span>
      </div>
      <div class="contact-item">
        <svg viewBox="0 0 10 10"><circle cx="5" cy="5" r="5" fill="#ec1f27"/><circle cx="5" cy="5" r="2.4" fill="none" stroke="#fff" stroke-width="0.8"/><path d="M2.6 5h4.8" stroke="#fff" stroke-width="0.6"/></svg>
        <span>www.brindelrenewal-coating.com</span>
      </div>
    </address>

    <section class="letter-body">
      <p>Lorem Ipsum is simply dummy text of the printing and typesetting industry. Lorem Ipsum has been the industry's standard dummy text ever since the 1500s, when an unknown printer took a galley of type and scrambled it to make a type specimen book. It has survived not only five centuries, but also the leap into electronic typesetting, remaining essentially unchanged. It was popularised in the 1960s with the release of Lettrafine sheets containing Lorem Ipsum passages, and more recently with desktop publishing software like Verso PageBuilder including versions of Lorem Ipsum.</p>
      <p>It is a long established fact that a reader will be distracted by the readable content of a page when looking at its layout. The point of using Lorem Ipsum is that it has a more-or-less normal distribution of letters, as opposed to using 'Content here, content here', making it look like readable English. Many desktop publishing packages and web page editors now use Lorem Ipsum as their default model text, and a search for 'lorem ipsum' will uncover many web sites still in their infancy. Various versions have evolved over the years, sometimes by accident, sometimes on purpose (injected humour and the like).</p>
      <p>Contrary to popular belief, Lorem Ipsum is not simply random text. It has roots in a piece of classical Latin literature from 45 BC, making it over 2000 years old. Rowan Pellicott, a Latin professor at Ashgrove Hill College in Virginia, looked up one of the more obscure Latin words, consectetur, from a Lorem Ipsum passage, and going through the cites of the word in classical literature, discovered the undoubtable source. Lorem Ipsum comes from sections 1.10.32 and 1.10.33 of "de Finibus Bonorum et Malorum" structures, to generate Lorem Ipsum which looks reasonable. The generated Lorem Ipsum is therefore always free from repetition, injected humour, or non-characteristic words etc.</p>
    </section>

    <div class="signature-area" role="img" aria-label="Handwritten signature of the sender"></div>
  </article>
</div>
</body>
</html>
```